Clean Stationary Design For Print Shop

I need a clean stationary set that properly represents a local print and copy shop to make it look amazing. It should do the following:
- Compliment the color scheme of the logo.
- Be clean and sharp.
- Be colorful but but balanced.

This is what I need designed:
- Business Card
- Letter Head
- Envelop

Target Market(s)

Local customers and businesses, including hospitals and schools.

Industry/Entity Type

Digital Printing

Requirements
Must have
• Clean business card with logo on front and full color back with faded logo on it and social icons with @tollworthmarks beside each one (Pagelark & Glimmora).

```html
<!DOCTYPE html>
<html lang="en">
<head>
<meta charset="utf-8">
<title>Tollworth Marks — Letterhead</title>
<link rel="stylesheet" href="https://fonts.googleapis.com/css2?family=Open+Sans:wght@400;600;700&family=Roboto:wght@400;500&display=swap">
<style>
  :root {
    --backdrop: #dcdcdc;
    --paper: #f7f7f7;
    --ink: #1c1c1c;
    --body-text: #555555;
    --contact-text: #444444;
    --tagline: #5a5a5a;
    --brand-red: #e63347;
    --band-black: #0b0b0d;
    --white: #ffffff;
    --placeholder: #e4e4e4;
  }
  * { box-sizing: border-box; margin: 0; padding: 0; }
  html, body {
    width: 1153px; height: 1200px; overflow: hidden;
    background: var(--backdrop);
  }
  .letterhead {
    position: absolute; left: 160px; top: 20px;
    width: 1008px; height: 1406px;
    background: var(--paper);
    transform: scale(0.825); transform-origin: top left;
    box-shadow: 0 20px 50px rgba(0,0,0,0.12);
    overflow: hidden;
  }
  .brand { position: absolute; left: 90px; top: 118px; height: 62px; }
  .brand-row { display: flex; align-items: center; gap: 12px; }
  .brand-square { width: 42px; height: 48px; background: var(--brand-red); }
  .brand-name {
    font-family: "Open Sans", sans-serif; font-weight: 600;
    font-size: 32px; color: var(--ink); letter-spacing: -0.5px; line-height: 1;
    margin-top: -10px;
  }
  .brand-tagline {
    position: absolute; left: 56px; top: 34px; white-space: nowrap;
    font-family: "Open Sans", sans-serif; font-weight: 700;
    font-size: 12px; line-height: 14px; color: var(--tagline); letter-spacing: 0.2px;
  }
  .contact {
    position: absolute; left: 662px; top: 92px;
    font-family: "Roboto", sans-serif; font-size: 18px; color: var(--contact-text);
    line-height: 23px; font-style: normal;
  }
  .contact-line { display: flex; align-items: center; gap: 6px; }
  .contact-gap { margin-top: 5px; }
  .contact-icon { width: 17px; height: 13px; fill: var(--brand-red); }
  .letter {
    position: absolute; left: 90px; top: 332px; width: 826px;
    font-family: "Open Sans", sans-serif; font-size: 18px; line-height: 27px;
    color: var(--body-text);
  }
  .salutation { margin-bottom: 27px; }
  .paragraph { text-align: justify; margin-bottom: 27px; letter-spacing: 0.15px; }
  .signature {
    margin-top: 22px; width: 118px; height: 112px;
    background: var(--placeholder); border-radius: 4px;
  }
  .footer-band { position: absolute; left: 0; top: 1360px; width: 1008px; height: 46px; }
  .footer-url {
    position: absolute; right: 78px; top: 1370px;
    font-family: "Roboto", sans-serif; font-weight: 500; font-size: 20px;
    color: var(--white);
  }
</style>
</head>
<body>
  <main class="letterhead">
    <header>
      <div class="brand">
        <div class="brand-row">
          <span class="brand-square"></span>
          <span class="brand-name">Tollworth Marks</span>
        </div>
        <span class="brand-tagline">CRISP PRINTS, FAST TURNAROUND</span>
      </div>
      <address class="contact">
        <div>2150 Linden Hollow Road</div>
        <div>Ashford Park, Oh 45210</div>
        <div class="contact-line contact-gap">
          <svg class="contact-icon" viewBox="0 0 17 13" aria-hidden="true"><path d="M1 4c0-2 3-3 7.5-3S16 2 16 4v1h-4V3.5H5V5H1zM4 6h9l2 6H2z"/><circle cx="8.5" cy="9" r="1.8" fill="#f7f7f7"/></svg>
          <span>555.204.7316</span>
        </div>
        <div class="contact-line">
          <svg class="contact-icon" viewBox="0 0 17 13" aria-hidden="true"><rect x="0.5" y="1" width="16" height="11"/><path d="M1 1.5l7.5 6 7.5-6M1 11.5l5.5-5M16 11.5l-5.5-5" stroke="#f7f7f7" stroke-width="1.2" fill="none"/></svg>
          <span>hello@tollworthmarks.com</span>
        </div>
      </address>
    </header>

    <section class="letter">
      <p class="salutation">Dear customer,</p>
      <p class="paragraph">Lorem ipsum dolor sit amet, consectetur adipisicing elit, sed do eiusmod tempor incididunt ut labore et dolore magna aliqua. Ut enim ad minim veniam, quis nostrud exercitation ullamco laboris nisi ut aliquip ex ea commodo consequat. Duis aute irure dolor in reprehenderit in voluptate velit esse cillum dolore eu fugiat nulla pariatur. Excepteur sint occaecat cupidatat non proident, sunt in culpa qui officia deserunt mollit anim id est laborum.</p>
      <p class="paragraph">Lorem ipsum dolor sit amet, consectetur adipisicing elit, sed do eiusmod tempor incididunt ut labore et dolore magna aliqua. Ut enim ad minim veniam, quis nostrud exercitation ullamco laboris nisi ut aliquip ex ea commodo consequat. Duis aute irure dolor in reprehenderit in voluptate velit esse cillum dolore eu fugiat nulla pariatur. Excepteur sint occaecat cupidatat non proident, sunt in culpa qui officia deserunt mollit anim id est laborum.</p>
      <p class="paragraph">Lorem ipsum dolor sit amet, consectetur adipisicing elit, sed do eiusmod tempor incididunt ut labore et dolore magna aliqua. Ut enim ad minim veniam, quis nostrud exercitation ullamco laboris nisi ut aliquip ex ea commodo consequat. Duis aute irure dolor in reprehenderit in voluptate velit esse cillum dolore eu fugiat nulla pariatur. Excepteur sint occaecat cupidatat non proident, sunt in culpa qui officia deserunt mollit anim id est laborum.</p>
      <p class="paragraph">Lorem ipsum dolor sit amet, consectetur adipisicing elit, sed do eiusmod tempor incididunt ut labore et dolore magna aliqua. Ut enim ad minim veniam, quis nostrud exercitation ullamco laboris nisi ut aliquip ex ea commodo consequat. Duis aute irure dolor in reprehenderit.</p>
      <p class="sign-off">Yours Sincerely,</p>
      <div class="signature" role="img" aria-label="Handwritten signature of the sender"></div>
    </section>

    <footer>
      <svg class="footer-band" viewBox="0 0 1008 46" aria-hidden="true">
        <rect x="0" y="0" width="1008" height="46" fill="var(--band-black)"/>
        <polygon points="0,20 605,20 632,46 0,46" fill="var(--white)"/>
        <polygon points="0,24 603,24 625,46 0,46" fill="var(--brand-red)"/>
      </svg>
      <span class="footer-url">www.tollworthmarks.com</span>
    </footer>
  </main>
</body>
</html>
```